Occupational Medical Billing and Coding Business needs Postcard

Medical billing and coding business needs marketing postcard to send to target audience of orthopaedic surgeons who practice medicine in California Workers' Compensation industry. These doctors treat injured workers and/or provide medical-legal evaluations and reports for the courts to settle the injured worker's claim. This is a highly specialized area of medical billing and coding. It is extremely complicated and can be very frustrating for doctors and their staff who do not understand the system. I would encourage the designers to check out my website: www.HollowbrookClaimServices.com
I want something bright and colorful that makes bold statements. It has to get their attention. My suggestions for bold statements include:
1) QMEs! Are your bills compliant with DWC's view? We make sure your complexity factors are maximized as well as compliant.
2) We collected over $ 462,000 just in second bill review (SBR) appeals alone and that's just one orthopaedic surgeon! Imagine what we can do for you!

I uploaded a word document with some information about the services I offer. The company logo is also there. Let me know if you need it in another format. The items with the asterisk (**) must be in the postcard.

Thank you so much!

Hollowbrook Claim Services

Target Market(s)

Orthopaedic Surgeons who treat injured workers in California

Font styles to use
Sans Serif

Colors

Designer to choose colors to be used in the design.

Requirements
Must have
• Expert Billing and Coding Services for:
• QME - AME - IME Evaluations
• Radiology - MRI/CT Scans
• Orthopaedic Surgery
• Certified Coders on Staff
• Electronic Claim Submission
• Payment within 15 days
• It's important to spell orthopaedic with the "A" after the "P" as it is an acknowledgment of the origins of the practice and will attract a doctor with higher education.

```html
<!DOCTYPE html>
<html lang="en">
<head>
<meta charset="utf-8">
<title>Hollowbrook Claim Services Postcard</title>
<link rel="stylesheet" href="https://fonts.googleapis.com/css2?family=Questrial&family=Lato:wght@700&display=swap">
<style>
  :root {
    --page: #ffffff;
    --ink: #3a3d4a;
    --ink-soft: #4a5060;
    --band: #353a4c;
    --teal: #74cfd7;
    --teal-pale: #b5e5ea;
    --photo-light: #e6f3f5;
    --photo-mid: #a9dde4;
    --photo-deep: #5fb8c4;
    --white: #ffffff;
    --button: #2f7fc7;
    --button-light: #4fa3e6;
    --icon: #2c7bc0;
  }
  * { margin: 0; padding: 0; box-sizing: border-box; }
  html, body { width: 810px; height: 1200px; overflow: hidden; background: var(--page); }
  body { position: relative; font-family: "Questrial", sans-serif; color: var(--ink); }

  .card { position: absolute; left: 31px; width: 718px; overflow: hidden; }
  .card--front { top: 30px; height: 548px; background: var(--teal); }
  .card--back { top: 589px; height: 548px; background: var(--teal-pale); border-left: 1px solid #9fd3da; }

  .hero-photo {
    position: absolute; left: 0; top: 0; width: 718px; height: 324px;
    background: linear-gradient(100deg, var(--photo-mid) 0%, var(--photo-light) 40%, var(--photo-light) 70%, var(--photo-mid) 100%);
  }
  .hero-photo::after {
    content: ""; position: absolute; left: 0; top: 0; width: 300px; height: 324px;
    background: radial-gradient(ellipse at 40% 55%, rgba(95,184,196,0.45), rgba(95,184,196,0) 70%);
  }

  .headline { position: absolute; left: 330px; width: 340px; text-align: center; color: var(--ink); }
  .headline__kicker { top: 52px; font-size: 29px; font-weight: 700; font-family: "Lato", sans-serif; }
  .headline__question { top: 100px; font-size: 23px; line-height: 32px; }
  .headline__question em { font-style: italic; }
  .headline__promise { top: 166px; font-size: 19px; line-height: 25px; color: var(--ink-soft); }
  .headline__url { top: 278px; font-family: "Lato", sans-serif; font-size: 13.5px; letter-spacing: 1.2px; }

  .tagline-band {
    position: absolute; left: 0; top: 324px; width: 718px; height: 40px;
    background: var(--band); color: var(--white);
    font-family: "Lato", sans-serif; font-variant: small-caps; font-size: 18px;
    line-height: 40px; text-align: center; letter-spacing: 0.2px;
  }

  .brand-name { position: absolute; color: var(--ink); font-family: "Questrial", sans-serif; }
  .brand-name--front { left: 34px; top: 398px; font-size: 40px; line-height: 46px; }
  .brand-name--back { left: 40px; top: 52px; font-size: 28px; line-height: 33px; }

  .service-list, .benefit-list { position: absolute; list-style: none; color: var(--ink-soft); }
  .service-list { left: 400px; top: 398px; font-size: 18px; line-height: 23.5px; }
  .benefit-list { left: 36px; top: 142px; font-size: 16.5px; line-height: 26px; }
  .service-list li, .benefit-list li { position: relative; padding-left: 20px; }
  .service-list li::before, .benefit-list li::before {
    content: "\2713"; position: absolute; left: 0; font-size: 0.85em;
  }
  .benefit-list .wrap { display: block; line-height: 20px; margin-bottom: 4px; }

  .contact-button { position: absolute; left: 112px; top: 314px; width: 120px; height: 70px; }

  .contact-line { position: absolute; left: 44px; display: flex; align-items: center; color: var(--ink); }
  .contact-line svg { width: 16px; height: 16px; margin-right: 14px; }
  .contact-line--phone { top: 393px; font-size: 25px; }
  .contact-line--email, .contact-line--web {
    font-family: "Lato", sans-serif; font-variant: small-caps; font-size: 14px; letter-spacing: 0.6px;
  }
  .contact-line--email { top: 431px; }
  .contact-line--web { top: 457px; }
</style>
</head>
<body>

<section class="card card--front">
  <div class="hero-photo" role="img" aria-label="Photo of a doctor in a white coat with a stethoscope touching a glowing medical interface with hexagons and a DNA helix"></div>

  <p class="headline headline__kicker">QMEs!</p>
  <p class="headline headline__question">Are your bills <em>compliant</em><br>with DWC's view?</p>
  <p class="headline headline__promise">We make sure your complexity<br>factors are maximized as well<br>as compliant!</p>
  <p class="headline headline__url">WWW.HOLLOWBROOKCLAIMSERVICES.COM</p>

  <div class="tagline-band">Expert Billing and Coding Services for Workers' Compensation Providers</div>

  <p class="brand-name brand-name--front">Hollowbrook<br>Claim Services</p>

  <ul class="service-list">
    <li>QME – AME – IME Evaluations</li>
    <li>Radiology – MRI/CT Scans</li>
    <li>Electrodiagnostic Studies</li>
    <li>Orthopaedic Surgery</li>
    <li>Ambulatory Surgery Centers</li>
  </ul>
</section>

<section class="card card--back">
  <p class="brand-name brand-name--back">Hollowbrook<br>Claim Services</p>

  <ul class="benefit-list">
    <li>Certified Coders on Staff</li>
    <li>Electronic Claim Submission</li>
    <li>Payment within 15 days</li>
    <li><span class="wrap">Over 25 Years Experience<br>in Workers' Comp</span></li>
    <li>We also provide Collection Services!</li>
  </ul>

  <svg class="contact-button" viewBox="0 0 120 70" aria-label="Contact us">
    <defs>
      <linearGradient id="buttonFill" x1="0" y1="0" x2="0" y2="1">
        <stop offset="0" stop-color="#4fa3e6"/>
        <stop offset="1" stop-color="#2f7fc7"/>
      </linearGradient>
    </defs>
    <path d="M4 4 L116 10 L114 52 L92 51 L98 66 L78 51 L2 48 Z" fill="url(#buttonFill)"/>
    <text x="60" y="36" text-anchor="middle" fill="#ffffff" font-family="Lato, sans-serif" font-weight="700" font-size="19" transform="rotate(3 60 30)">contact us</text>
  </svg>

  <p class="contact-line contact-line--phone">
    <svg viewBox="0 0 16 16" aria-hidden="true"><circle cx="8" cy="8" r="6.5" fill="none" stroke="var(--icon)" stroke-width="1.4"/><path d="M6 4.5 L7.5 6.5 L6.8 7.5 Q7.5 9 9 9.6 L10 8.8 L11.6 10.3 L10.6 11.6 Q6 11 4.8 6 Z" fill="var(--icon)"/></svg>
    714. 555.0182
  </p>
  <p class="contact-line contact-line--email">
    <svg viewBox="0 0 16 16" aria-hidden="true"><rect x="3" y="4" width="12" height="8" fill="none" stroke="var(--icon)" stroke-width="1.3"/><path d="M3 4 L9 9 L15 4" fill="none" stroke="var(--icon)" stroke-width="1.3"/><path d="M0 6 H2 M0 9 H2" stroke="var(--icon)" stroke-width="1.2"/></svg>
    info@HollowbrookClaimServices.com
  </p>
  <p class="contact-line contact-line--web">
    <svg viewBox="0 0 16 16" aria-hidden="true"><circle cx="8" cy="8" r="6.5" fill="none" stroke="var(--icon)" stroke-width="1.3"/><ellipse cx="8" cy="8" rx="3" ry="6.5" fill="none" stroke="var(--icon)" stroke-width="1.1"/><path d="M1.5 8 H14.5 M2.8 4.6 H13.2 M2.8 11.4 H13.2" stroke="var(--icon)" stroke-width="1"/></svg>
    www.HollowbrookClaimServices.com
  </p>
</section>

</body>
</html>
```